Quill Scholars Homepage and Landing Page Redesign

Quill Scholars 789 is a premier test preparation, academic consultation, and private tutoring company based in Los Angeles. We offer our tutoring in-person and also online. <br/><br/>We will need three mockups that are as follows:<br/><br/>1. A mockup of a homepage that will be on www.quillscholars789.com<br/>2. A mockup of a free-standing true landing page that will be a one-page site where we will direct traffic from a Google PPC ad.<br/>3. A mockup of a landing page that will replace a landing page such as the one at www.quillscholars789.com/test-prep-services/k-12/sat/ <br/><br/>Please see the word attached for details.

Target Market(s)

Middle School and High School Student Parents, College Students.

Industry/Entity Type

Tutoring

Number of Pages Required

3 page

Colors

Designer to choose colors to be used in the design.

Requirements
Must have
• The design of these 3 pages will need to fit within the overall design of the main website. We're looking for a user-friendly, easy-to-navigate, yet professional design.

```html
<!DOCTYPE html>
<html lang="en">
<head>
<meta charset="utf-8">
<title>Quill Scholars – Tutors &amp; Contact</title>
<link href="https://fonts.googleapis.com/css2?family=Josefin+Sans:wght@400;600;700&family=Open+Sans:wght@400;600&display=swap" rel="stylesheet">
<style>
:root{
  --coral:#ef7d56;
  --teal:#2c93a7;
  --white:#ffffff;
  --wave:#f7f7f7;
  --footer:#eeeeee;
  --ink:#333333;
  --muted:#5a5a5a;
  --link-head:#8390d6;
  --navy:#1d4e63;
}
*{margin:0;padding:0;box-sizing:border-box}
html,body{width:922px;height:1200px;overflow:hidden;background:var(--white)}
.page{position:relative;width:922px;height:1200px;overflow:hidden;font-family:"Open Sans",sans-serif;color:var(--ink)}
.abs{position:absolute}

.tutors-title{left:0;width:922px;top:98px;text-align:center;font-family:"Josefin Sans",sans-serif;font-weight:700;font-size:31px;letter-spacing:1.5px;color:var(--coral)}

.tutor-card{top:165px;width:192px;height:243px;background:var(--white);box-shadow:0 2px 5px rgba(0,0,0,.3);border-radius:2px;overflow:hidden}
.tutor-photo{position:absolute;left:0;top:0;width:100%;height:186px}
.photo-suit{background:radial-gradient(ellipse 38% 30% at 50% 38%,#d9a98c 0%,#d9a98c 55%,rgba(217,169,140,0) 100%),linear-gradient(180deg,#ffffff 0%,#ffffff 45%,#2b3142 80%,#1f2433 100%)}
.photo-light{background:radial-gradient(ellipse 40% 34% at 50% 36%,#e8b99c 0%,#e8b99c 50%,rgba(232,185,156,0) 100%),linear-gradient(180deg,#ffffff 0%,#f1dfa6 35%,#d8c58a 60%,#b9c6d6 100%)}
.photo-shirt{background:radial-gradient(ellipse 36% 30% at 52% 38%,#d8a88a 0%,#d8a88a 50%,rgba(216,168,138,0) 100%),linear-gradient(180deg,#ffffff 0%,#ffffff 40%,#4a5c9a 72%,#3c4d8a 100%)}
.photo-stripe{background:radial-gradient(ellipse 34% 30% at 50% 34%,#eec3aa 0%,#eec3aa 50%,rgba(238,195,170,0) 100%),linear-gradient(180deg,#ffffff 0%,#8a5d43 30%,#9a6c50 60%,#c4cde0 100%)}
.tutor-caption{position:absolute;left:0;top:186px;width:100%;height:57px;color:var(--white);font-family:"Josefin Sans",sans-serif;font-weight:600;font-size:10.4px;letter-spacing:.8px;text-align:center;line-height:11.6px;padding-top:4px;white-space:nowrap}
.tutor-caption .gap{display:block;height:2.5px}
.coral{background:var(--coral)}
.teal{background:var(--teal)}

.btn{display:flex;align-items:center;justify-content:center;background:var(--coral);color:var(--white);font-family:"Josefin Sans",sans-serif;font-weight:700;letter-spacing:1.2px;border-radius:30px}
.see-more{left:347px;top:455px;width:228px;height:56px;font-size:19.5px;padding-top:3px}

.contact{left:0;top:562px;width:922px;height:450px;background:var(--teal)}
.contact-title{left:0;width:922px;top:580px;text-align:center;font-family:"Josefin Sans",sans-serif;font-weight:700;font-size:31px;letter-spacing:2px;color:var(--white)}
.field{width:364px;height:51px;background:var(--white);border-radius:4px;font-size:21.5px;color:var(--muted);letter-spacing:.6px;padding-left:8px;display:flex;align-items:center}
.field.low{align-items:flex-end;padding-bottom:5px}
.field.right{padding-left:10px}
.send{left:359px;top:818px;width:203px;height:50px;font-size:18.5px;padding-top:3px}

.waves{left:0;top:840px;width:922px;height:172px}

.footer{left:0;top:1011px;width:922px;height:189px;background:var(--footer)}
.brand{left:50px;top:1046px;display:flex;align-items:center;gap:5px;font-family:"Open Sans",sans-serif;font-weight:600;font-size:17px;color:var(--navy)}
.brand-dot{width:10px;height:10px;border-radius:50%;background:var(--teal)}
.address{left:50px;top:1086px;font-size:10px;line-height:14px}
.about{left:187px;top:1048px;width:200px;font-size:10px;line-height:14px}
.col-head{font-size:9.6px;color:var(--link-head);letter-spacing:.2px}
.col-list{list-style:none;margin-top:12px;font-size:10px;line-height:15.4px}
.services{left:411px;top:1049px}
.more{left:532px;top:1049px}
.subscribe{left:671px;top:1043px;width:191px}
.subscribe h3{font-weight:400;font-size:15.5px;color:var(--coral);letter-spacing:.4px}
.subscribe .label{margin-top:11px;font-size:10px;color:var(--ink)}
.sub-input{position:relative;margin-top:12px;width:191px;height:23px;background:var(--white);border-bottom:1px solid #dcdcdc}
.sub-input svg{position:absolute;right:6px;top:6px}
.sub-btn{margin-top:16px;width:66px;height:25px;background:var(--navy);color:var(--white);font-size:11.5px;display:flex;align-items:center;justify-content:center;border-radius:2px}
</style>
</head>
<body>
<main class="page">

  <h2 class="abs tutors-title">Meet Some Of Our Experienced Tutors</h2>

  <article class="abs tutor-card" style="left:33px">
    <div class="tutor-photo photo-suit" role="img" aria-label="Portrait photo of tutor Owen P. in a dark blazer"></div>
    <div class="tutor-caption coral">OWEN P.<br>Specializes in ISEE<span class="gap"></span>Pacific Institute of Science<br>Ph.D. candidate</div>
  </article>
  <article class="abs tutor-card" style="left:252px">
    <div class="tutor-photo photo-light" role="img" aria-label="Portrait photo of tutor Leah M. in a light blue shirt"></div>
    <div class="tutor-caption teal">LEAH M.<br>Specializes in ACT<span class="gap"></span>Hollins Ridge College<br>B.E in Mechanical Engineering</div>
  </article>
  <article class="abs tutor-card" style="left:470px">
    <div class="tutor-photo photo-shirt" role="img" aria-label="Portrait photo of tutor Adam R. in a blue shirt"></div>
    <div class="tutor-caption coral">ADAM R.<br>Specializes in HSPT<span class="gap"></span>Marlow University<br>B.A. in Literature</div>
  </article>
  <article class="abs tutor-card" style="left:689px">
    <div class="tutor-photo photo-stripe" role="img" aria-label="Portrait photo of tutor Nora K. in a striped shirt"></div>
    <div class="tutor-caption teal">NORA K.<br>Specializes in SAT<span class="gap"></span>Westbrook University<br>B.A. in Politics</div>
  </article>

  <div class="abs btn see-more">SEE MORE TUTORS</div>

  <section class="abs contact"></section>
  <h2 class="abs contact-title">CONTACT US TODAY</h2>

  <div class="abs field" style="left:69px;top:653px">Name</div>
  <div class="abs field right" style="left:467px;top:653px">Email</div>
  <div class="abs field low" style="left:69px;top:741px">Phone</div>
  <div class="abs field low right" style="left:467px;top:741px">School</div>

  <svg class="abs waves" viewBox="0 840 922 172" aria-hidden="true">
    <defs>
      <radialGradient id="glow" cx="50%" cy="50%" r="50%">
        <stop offset="0" stop-color="#f6c56a" stop-opacity=".45"/>
        <stop offset="1" stop-color="#f6c56a" stop-opacity="0"/>
      </radialGradient>
    </defs>
    <path fill="var(--wave)" d="M0 911 C10 950 30 980 60 975 C95 970 100 930 102 915 C106 895 130 880 150 892 C165 900 175 910 188 905 C210 890 230 850 280 848 C315 847 322 880 330 905 C340 935 360 945 385 940 C410 935 420 905 435 893 C450 880 470 880 485 895 C495 905 495 940 510 960 C525 975 555 975 572 955 C585 935 585 910 605 905 C630 900 650 915 660 935 C675 970 690 995 715 994 C740 993 760 960 768 930 C780 895 800 875 830 868 C860 862 895 864 922 872 L922 1012 L0 1012 Z"/>
    <ellipse cx="240" cy="930" rx="48" ry="40" fill="url(#glow)"/>
    <ellipse cx="680" cy="975" rx="30" ry="26" fill="url(#glow)"/>
    <circle cx="219" cy="907" r="39" fill="var(--coral)"/>
    <circle cx="666" cy="958" r="25" fill="var(--coral)"/>
  </svg>

  <div class="abs btn send">SEND EMAIL NOW</div>

  <footer class="abs footer"></footer>

  <div class="abs brand"><span class="brand-dot"></span>Quill Scholars</div>
  <address class="abs address" style="font-style:normal">
    4120 Larkspur Ave.<br>Suite 210<br>Fernwood, CA 90000<br>555-014-2738<br>hello@quillscholars789.com
  </address>

  <p class="abs about">Quill Scholars 789 is a premier test preparation, academic consultation, and private tutoring company in Los Angeles.<br><br>We specialize in SAT, ACT, ISEE, HSPT, CHSPE, GRE, GMAT, CBEST, and CSET prep as well as academic tutoring in Math, Science, English, and Social Studies.</p>

  <nav class="abs services">
    <div class="col-head">POPULAR SERVICES</div>
    <ul class="col-list"><li>SAT</li><li>ACT</li><li>ISEE</li><li>CHSPE</li><li>GMAT</li><li>CSET</li></ul>
  </nav>
  <nav class="abs more">
    <div class="col-head">MORE INFO</div>
    <ul class="col-list"><li>Tutoring Resources</li><li>FAQ</li><li>Blog</li><li>Tutoring Jobs</li><li>Innovation Scholarship</li><li>Free Diagnostic Test</li></ul>
  </nav>

  <div class="abs subscribe">
    <h3>SUBSCRIBE</h3>
    <div class="label">Your Email Address</div>
    <div class="sub-input">
      <svg width="12" height="10" viewBox="0 0 12 10" aria-hidden="true"><path d="M1 8 L11 2 M5 3 L11 2 L9 7" stroke="var(--teal)" stroke-width="1.4" fill="none"/></svg>
    </div>
    <div class="sub-btn">Subscribe</div>
  </div>

</main>
</body>
</html>
```